Design for New Hosting Business

We are looking for a hosting site design for our new business. We don't currently have a logo but would like the site to operate like brambleworks.co.uk

Industry/Entity Type

Business

```html
<!DOCTYPE html>
<html lang="en">
<head>
<meta charset="utf-8">
<title>CoreBay Hosting</title>
<link href="https://fonts.googleapis.com/css2?family=Source+Sans+3:wght@400;600;700&family=Arimo:ital,wght@0,700;1,700&display=swap" rel="stylesheet">
<style>
:root{
  --page:#f3f3f3;
  --ink:#2b2b2b;
  --ink-soft:#3a3a3a;
  --white:#ffffff;
  --accent:#f2c417;
  --accent-deep:#b98b0a;
  --hero-dark:#141414;
  --hero-mid:#3c3c3c;
  --nav-top:#3d3d3d;
  --nav-bottom:#050505;
  --card-line:#e2e2e2;
  --testimonial:#4a4a4a;
  --muted:#8a8a8a;
  --text-font:"Source Sans 3",sans-serif;
  --head-font:"Arimo",sans-serif;
}
*{margin:0;padding:0;box-sizing:border-box}
html,body{width:1200px;height:1129px;overflow:hidden}
body{background:var(--page);font-family:var(--text-font);color:var(--ink);position:relative}

.site-header{position:absolute;left:0;top:0;width:1200px;height:152px;background:linear-gradient(#ffffff,#e3e3e3)}
.utility-links{position:absolute;right:26px;top:9px;font-size:13px;color:var(--ink)}
.brand{position:absolute;left:68px;top:36px;display:flex;align-items:center;gap:12px}
.brand-mark{width:44px;height:44px;border-radius:50%;background:var(--ink-soft)}
.brand-name{font-size:50px;font-weight:600;color:var(--ink-soft);letter-spacing:-0.5px;line-height:1}
.phone{position:absolute;left:985px;top:44px;display:flex;align-items:center;gap:9px;font-size:25px;color:var(--ink)}
.main-nav{position:absolute;left:378px;top:110px;display:flex;gap:3px}
.main-nav a{display:block;height:42px;line-height:42px;text-align:center;color:var(--white);text-decoration:none;font-size:20px;background:linear-gradient(var(--nav-top),var(--nav-bottom));border-radius:4px 4px 0 0;border:1px solid #000}

.hero{position:absolute;left:0;top:152px;width:1200px;height:356px;background:linear-gradient(115deg,var(--hero-dark) 0%,var(--hero-mid) 32%,#2a2a2a 55%,#474747 80%,#1e1e1e 100%);overflow:visible}
.hero-title{position:absolute;left:66px;top:44px;font-size:44px;font-weight:400;color:var(--white);letter-spacing:0.5px}
.hero-sub{position:absolute;left:66px;top:98px;font-size:23px;color:var(--accent)}
.hero-list{position:absolute;left:66px;top:134px;list-style:none;color:var(--white);font-size:20px;line-height:35px}
.hero-art{position:absolute;left:452px;top:38px;width:222px;height:332px;background:linear-gradient(100deg,#1b1b1b,#8c8c8c 45%,#2e2e2e 70%,#6a6a6a);border-radius:6px}

.offer{position:absolute;left:760px;top:208px;width:350px;height:268px;border-radius:6px;background:linear-gradient(#f7cd1c,#f0c115 55%,var(--accent-deep));box-shadow:0 2px 6px rgba(0,0,0,.5)}
.price{position:absolute;left:24px;top:32px;color:var(--ink);font-family:var(--text-font);font-weight:700;line-height:1;display:flex;align-items:flex-start}
.price .cur{font-size:42px;margin-top:8px}
.price .whole{font-size:76px}
.price .cents{font-size:42px;margin-top:8px}
.offer-points{position:absolute;left:174px;top:14px;list-style:none;font-size:21px;line-height:35px;color:var(--ink)}
.offer-text{position:absolute;left:31px;top:122px;width:300px;font-size:15px;line-height:22px;color:var(--ink-soft)}
.btn{position:absolute;top:206px;width:102px;height:34px;border-radius:5px;color:var(--white);font-family:var(--head-font);font-style:italic;font-weight:700;font-size:15px;text-align:center;line-height:34px;text-decoration:none}
.btn-order{left:57px;background:#0d0d0d}
.btn-learn{left:183px;background:linear-gradient(#6a6a6a,#3c3c3c)}

.perks{position:absolute;left:34px;top:532px;width:337px;height:219px;background:var(--white);border:1px solid var(--card-line);border-radius:8px;padding:0 20px}
.perk{display:flex;align-items:center;gap:18px;height:61px;border-bottom:1px solid var(--card-line);font-size:20px;line-height:21px;color:var(--ink)}
.perk:first-child{margin-top:10px;height:62px}
.perk:last-child{border-bottom:none}
.perk svg{flex:none}

.welcome{position:absolute;left:411px;top:536px;width:752px}
.welcome h2{font-family:var(--head-font);font-weight:700;font-size:28px;color:var(--ink);margin-left:3px}
.welcome p{font-size:15px;line-height:23.3px;color:var(--ink);margin-top:4px}

.testimonials{position:absolute;left:34px;top:776px;width:336px;height:240px;background:var(--testimonial);border-radius:8px;color:var(--white)}
.testimonials h2{position:absolute;left:24px;top:16px;font-size:29px;font-weight:600}
.testimonials .quote-mark{position:absolute;left:22px;top:42px;font-size:54px;color:var(--muted);font-family:Georgia,serif}
.testimonials p{position:absolute;left:58px;top:60px;width:264px;font-size:15px;line-height:22.5px}

.datacenter{position:absolute;left:418px;top:771px;width:748px;height:240px;border-radius:8px;background:linear-gradient(#ededed,#e2e2e2);box-shadow:0 2px 4px rgba(0,0,0,.25)}
.datacenter h2{position:absolute;left:17px;top:12px;font-size:28px;font-weight:600;color:var(--ink);z-index:1}
.datacenter-art{position:absolute;left:55px;top:27px;width:287px;height:213px;background:radial-gradient(circle at 55% 40%,#5d9ad6 0,#dfe8f2 28%,#ffffff 50%,#f4f4f4 100%)}
.datacenter p{position:absolute;left:342px;top:52px;width:385px;font-size:15px;line-height:23px;color:var(--ink)}

.site-footer{position:absolute;left:0;top:1056px;width:1200px;height:73px;background:linear-gradient(#3c3c3c,#111);color:var(--white);font-size:15px;text-align:center;line-height:88px}
</style>
</head>
<body>

<header class="site-header">
  <div class="utility-links">Login | Sitemap</div>
  <div class="brand"><span class="brand-mark"></span><span class="brand-name">CoreBay</span></div>
  <div class="phone">
    <svg width="16" height="24" viewBox="0 0 16 24" aria-hidden="true"><path d="M5 1c2 0 3 4 3 6s-3 2-3 3 2 6 4 7 2-2 4-1 3 3 2 5-4 3-6 1C5 19 1 13 1 7 1 3 3 1 5 1z" fill="#8a8a8a"/></svg>
    <span>555-210-4830</span>
  </div>
  <nav class="main-nav">
    <a href="#" style="width:112px">HOME</a>
    <a href="#" style="width:141px">COMPANY</a>
    <a href="#" style="width:121px">HOSTING</a>
    <a href="#" style="width:127px">NETWORK</a>
    <a href="#" style="width:124px">SUPPORT</a>
    <a href="#" style="width:151px">CONTACT US</a>
  </nav>
</header>

<section class="hero">
  <h1 class="hero-title">QUALITY &amp; SPEED</h1>
  <p class="hero-sub">Quality server and fastest connection</p>
  <ul class="hero-list">
    <li>&gt; 1000 MB of storage Space</li>
    <li>&gt; 1000 MB Of Monthly Transfer</li>
    <li>&gt; CPANEL Access</li>
    <li>&gt; Unlimited Domain Name</li>
    <li>&gt; Unlimted Email</li>
  </ul>
  <div class="hero-art" role="img" aria-label="Two black server towers"></div>

  <div class="offer" style="top:56px">
    <div class="price"><span class="cur">$</span><span class="whole">4</span><span class="cents">.95</span></div>
    <ul class="offer-points">
      <li>&gt; No Contract</li>
      <li>&gt; No Hidden Fess</li>
      <li>&gt; Free Setup</li>
    </ul>
    <p class="offer-text">Lorem ipsum dolor sit amet, consectetur adipiscing elit. Cras felis lorem, ultricies nec volutpat id, consequat vel ante.</p>
    <a class="btn btn-order" href="#">Order Now</a>
    <a class="btn btn-learn" href="#">Learn More</a>
  </div>
</section>

<aside class="perks">
  <div class="perk">
    <svg width="42" height="42" viewBox="0 0 42 42" aria-hidden="true"><rect x="3" y="6" width="36" height="33" rx="3" fill="#fff" stroke="#bbb"/><rect x="3" y="6" width="36" height="10" rx="3" fill="#d43a2a"/><text x="21" y="34" font-size="16" font-weight="700" text-anchor="middle" fill="#333" font-family="Arial,sans-serif">30</text></svg>
    <span>30 Day Money Back<br>Guarntee</span>
  </div>
  <div class="perk">
    <svg width="42" height="42" viewBox="0 0 42 42" aria-hidden="true"><rect x="4" y="28" width="6" height="12" fill="#aaa"/><rect x="13" y="22" width="6" height="18" fill="#999"/><rect x="22" y="14" width="6" height="26" fill="#888"/><rect x="31" y="6" width="6" height="34" fill="#5aa83a"/></svg>
    <span>99.9% Uptime Guarneed!</span>
  </div>
  <div class="perk">
    <svg width="42" height="42" viewBox="0 0 42 42" aria-hidden="true"><circle cx="21" cy="21" r="18" fill="#f0a020"/><circle cx="21" cy="21" r="14" fill="#fff"/><path d="M21 11v10h7" stroke="#333" stroke-width="2.5" fill="none"/></svg>
    <span>10 Minutes Support<br>Response</span>
  </div>
</aside>

<section class="welcome">
  <h2>Welcome</h2>
  <p>Lorem ipsum dolor sit amet, consectetur adipiscing elit. Cras felis lorem, ultricies nec volutpat id, consequat vel ante. Phasellus in aliquam est. Praesent sodales justo ut orci tempus egestas. Donec risus nulla, dictum nec commodo a, lacinia a nibh. Nulla id hendrerit lorem. Morbi laoreet lectus nec mi vehicula sit amet feugiat nunc vestibulum. Fusce vel augue non orci vehicula ullamcorper. Curabitur hendrerit cursus sem, porttitor cursus tellus pulvinar volutpat. Duis a tellus nibh. Fusce nulla nunc, vehicula hendrerit blandit at, mattis id sem. Cras ac dolor sit amet felis tempus volutpat quis at arcu. Ut at dolor nec tortor lobortis dictum. Nam odio enim, malesuada eu blandit vitae, scelerisque a erat. Donec malesuada suscipit aliquam. Fusce sagittis accumsan.</p>
</section>

<section class="testimonials">
  <h2>Testimonials</h2>
  <span class="quote-mark">&ldquo;</span>
  <p>Lorem ipsum dolor sit amet, consectetur adipiscing elit. Cras felis lorem, ultricies nec volutpat id, consequat vel ante. Phasellus in aliquam est. Praesent sodales justo ut orci tempus egestas. Donec risus nullahendrerit</p>
</section>

<section class="datacenter">
  <h2>Our Data Center</h2>
  <div class="datacenter-art" role="img" aria-label="Ring of server racks around a blue globe"></div>
  <p>Lorem ipsum dolor sit amet, consectetur adipiscing elit. Cras felis lorem, ultricies nec volutpat id, consequat vel ante. Phasellus in aliquam est. Praesent sodales justo ut orci tempus egestas. Donec risus nulla, dictum nec commodo a, lacinia a nibh. Nulla id hendrerit lorem. Morbi laoreet lectus nec mi vehicula sit amet feugiat nunc vestibulum. Fusce vel augue non orci vehicula ullamcorper.</p>
</section>

<footer class="site-footer">Copyright 2011 CoreBay. All Rights Reserved | Privacy Policy</footer>

</body>
</html>
```